Business Card Design

We need a business card design for a new dental practice in Brisbane. I'd like the basic details and logo on one side and appointment schedule on the other side. It is based in CBD office area and would prefer a professional and modern design.
Target Market(s)
20-60 years old office workers and residents with high education levels
Industry/Entity Type
Dental
Contact Information for Business Card
Harbourlight Dental
Dr Marcus Lund
Principal Dentist
07 3619 4827
admin@harbourlightdentistry.com.au
www.harbourlightdentistry.com.au
S7, Level 2, Amberly North Building, 318 Garnett Rd, Kelvin Reach, QLD 4011

```html
<!DOCTYPE html>
<html lang="en">
<head>
<meta charset="utf-8">
<title>Harbourlight Dental – Business Card</title>
<link href="https://fonts.googleapis.com/css2?family=Questrial&display=swap" rel="stylesheet">
<style>
  :root {
    --stage: #e4e6e8;
    --card: #f5f6f7;
    --ink: #1d1f24;
    --brand-blue: #3aa0d8;
    --accent-cyan: #29b3d6;
    --navy: #0f2a3e;
    --muted-dots: #5cc3dd;
  }
  * { margin: 0; padding: 0; box-sizing: border-box; }
  html, body {
    width: 1200px;
    height: 516px;
    overflow: hidden;
    background: var(--stage);
    font-family: "Questrial", "Century Gothic", sans-serif;
    color: var(--ink);
  }
  .stage {
    position: relative;
    width: 1200px;
    height: 516px;
    display: flex;
    justify-content: center;
    align-items: center;
    gap: 40px;
  }
  .card {
    position: relative;
    width: 540px;
    height: 308px;
    background: var(--card);
    box-shadow: 0 6px 18px rgba(0, 0, 0, 0.18);
    overflow: hidden;
  }

  /* Front */
  .brand {
    position: absolute;
    left: 22px;
    top: 90px;
    width: 236px;
    display: flex;
    flex-direction: column;
    align-items: center;
    gap: 14px;
  }
  .brand-dot {
    width: 60px;
    height: 60px;
    border-radius: 50%;
    background: var(--brand-blue);
  }
  .brand-name {
    font-size: 25px;
    color: var(--brand-blue);
    white-space: nowrap;
  }
  .details {
    position: absolute;
    left: 278px;
    top: 44px;
  }
  .person-name {
    font-size: 15px;
    letter-spacing: 0.3px;
    line-height: 18px;
  }
  .person-role {
    font-size: 12.5px;
    color: var(--brand-blue);
    line-height: 16px;
  }
  .address {
    margin-top: 26px;
    font-size: 12.5px;
    line-height: 16px;
    font-style: normal;
  }
  .contacts {
    margin-top: 30px;
    list-style: none;
    font-size: 12.5px;
    line-height: 16px;
  }
  .contacts li {
    display: flex;
    align-items: center;
    gap: 5px;
  }
  .contacts svg { width: 10px; height: 10px; flex: none; }
  .wave {
    position: absolute;
    left: 0;
    bottom: 0;
    width: 540px;
    height: 308px;
  }

  /* Back */
  .appointment-title {
    position: absolute;
    top: 50px;
    width: 100%;
    text-align: center;
    font-size: 15px;
  }
  .slots {
    position: absolute;
    left: 112px;
    top: 86px;
    list-style: none;
    color: var(--accent-cyan);
    font-size: 13px;
    letter-spacing: 0.4px;
  }
  .slot {
    height: 14px;
    white-space: nowrap;
  }
  .slot:nth-child(1) { margin-top: 0; }
  .slot:nth-child(2) { margin-top: 23px; }
  .slot:nth-child(3) { margin-top: 19px; }
  .slot:nth-child(4) { margin-top: 20px; }
  .slot:nth-child(5) { margin-top: 27px; }
  .slot .dots { color: var(--muted-dots); }
</style>
</head>
<body>
<main class="stage">
  <section class="card card-front" aria-label="Card front">
    <div class="brand">
      <span class="brand-dot"></span>
      <span class="brand-name">Harbourlight Dental</span>
    </div>

    <div class="details">
      <p class="person-name">DR MARCUS LUND</p>
      <p class="person-role">Principal Dentist</p>
      <address class="address">
        S7, Level 2, Amberly North Building,<br>
        318 Garnett Rd,<br>
        Kelvin Reach, QLD 4011
      </address>
      <ul class="contacts">
        <li>
          <svg viewBox="0 0 10 10" aria-hidden="true"><rect x="2.5" y="0.5" width="5" height="9" rx="1" fill="none" stroke="var(--brand-blue)" stroke-width="1.2"/></svg>
          07 3619 4827
        </li>
        <li>
          <svg viewBox="0 0 10 10" aria-hidden="true"><rect x="0.5" y="2" width="9" height="6" rx="1" fill="var(--brand-blue)"/><path d="M0.8 2.5 L5 5.5 L9.2 2.5" fill="none" stroke="#fff" stroke-width="0.8"/></svg>
          admin@harbourlightdentistry.com.au
        </li>
        <li>
          <svg viewBox="0 0 10 10" aria-hidden="true"><circle cx="5" cy="5" r="4.5" fill="var(--brand-blue)"/><path d="M0.5 5 H9.5 M5 0.5 V9.5" stroke="#fff" stroke-width="0.6"/></svg>
          www.harbourlightdentistry.com.au
        </li>
      </ul>
    </div>

    <svg class="wave" viewBox="0 0 540 308" aria-hidden="true">
      <path d="M0 308 L0 293 Q270 234 540 298 L540 308 Z" fill="var(--navy)"/>
      <path d="M0 283 Q270 224 540 290" fill="none" stroke="var(--brand-blue)" stroke-width="3"/>
    </svg>
  </section>

  <section class="card card-back" aria-label="Card back">
    <p class="appointment-title">Your appointment with Dr Marcus Lund</p>
    <ul class="slots">
      <li class="slot">DATE <span class="dots">.....................</span>&nbsp; TIME <span class="dots">......................</span> AM | PM</li>
      <li class="slot">DATE <span class="dots">.....................</span>&nbsp; TIME <span class="dots">......................</span> AM | PM</li>
      <li class="slot">DATE <span class="dots">.....................</span>&nbsp; TIME <span class="dots">......................</span> AM | PM</li>
      <li class="slot">DATE <span class="dots">.....................</span>&nbsp; TIME <span class="dots">......................</span> AM | PM</li>
      <li class="slot">DATE <span class="dots">.....................</span>&nbsp; TIME <span class="dots">......................</span> AM | PM</li>
    </ul>
  </section>
</main>
</body>
</html>
```